Q & Q Fabrications HVAC Mechanical Contractor Business Card

We need a business card for a HVAC/Plumbing Mechanical Contractor. Our website is http://www.qqfabrications-example.com. We would like to include the picture of the person on the card. Pictures of people for mock-ups can be found on our website. The blue on our logo is our primary color. We'd like this to be bold yet professional without too many colors but with some color to make sure it stands out.

Industry/Entity Type

Business

Contact Information for Business Card

Font styles to use
Sans Serif

Colors
000000

Requirements
Must have
• Our logo
• Person's picture
• Company Name
• Company Phone
• Person's email address
• Person's phone number
Nice to have
• Company Address
Should not have
• Clip art

```html
<!DOCTYPE html>
<html lang="en">
<head>
<meta charset="utf-8">
<title>Q&amp;Q Fabrications – Business Card</title>
<link href="https://fonts.googleapis.com/css2?family=Arimo:wght@400;700&display=swap" rel="stylesheet">
<style>
  :root {
    --page-bg: #e9e9e9;
    --brand-blue: #3a82c9;
    --brand-blue-light: #5aa3dd;
    --brand-blue-dark: #2a64a6;
    --card-dark: #2b2b2d;
    --card-mid: #3a3a3c;
    --panel-light: #a9a9ab;
    --panel-dark: #767678;
    --text-white: #ffffff;
    --text-soft: #e6e6e6;
    --logo-black: #111111;
  }
  * { margin: 0; padding: 0; box-sizing: border-box; }
  html, body { width: 1200px; height: 1000px; overflow: hidden; }
  body {
    background: var(--page-bg);
    font-family: "Arimo", Arial, sans-serif;
    display: flex; align-items: center; justify-content: center;
  }
  .card {
    position: relative;
    width: 1000px; height: 580px;
    background: linear-gradient(100deg, var(--card-dark) 0%, var(--card-mid) 55%, #4a4a4c 100%);
    box-shadow: 0 12px 30px rgba(0,0,0,.25);
    overflow: hidden;
  }
  .brand-band {
    position: absolute; left: 0; top: 0; width: 100%; height: 150px;
    background: linear-gradient(90deg, var(--brand-blue-dark) 0%, var(--brand-blue) 45%, var(--brand-blue-light) 100%);
    display: flex; align-items: center; padding-left: 30px; gap: 34px;
  }
  .brand-mark {
    width: 112px; height: 112px;
    background: var(--logo-black);
    border: 4px solid var(--text-white);
  }
  .company-name {
    color: var(--text-white); font-weight: 700; font-size: 72px; letter-spacing: .5px;
    white-space: nowrap;
  }
  .person-row {
    position: absolute; left: 330px; right: 40px; top: 168px;
    display: flex; align-items: flex-end; justify-content: space-between;
    border-bottom: 3px solid var(--text-white); padding-bottom: 8px;
  }
  .person-name { color: var(--text-white); font-weight: 700; font-size: 32px; }
  .person-title { color: var(--text-soft); font-size: 21px; }
  .portrait {
    position: absolute; left: 40px; top: 250px;
    width: 250px; height: 250px; border-radius: 50%;
    border: 4px solid var(--text-white);
    background: radial-gradient(circle at 45% 40%, #b9b9b9 0%, #8a8a8a 55%, #5e5e60 100%);
  }
  .contact-panel {
    position: absolute; left: 410px; top: 238px; width: 560px; height: 290px;
    background: linear-gradient(135deg, var(--panel-light) 0%, var(--panel-dark) 100%);
    padding: 22px 0 0 0;
  }
  .contact-list { list-style: none; }
  .contact-item {
    display: flex; align-items: center; gap: 18px;
    height: 50px; color: var(--text-white); font-size: 22px;
  }
  .contact-icon {
    width: 40px; height: 40px; margin-left: -20px;
    background: var(--brand-blue);
    display: flex; align-items: center; justify-content: center;
    box-shadow: 0 2px 3px rgba(0,0,0,.3);
  }
  .contact-icon svg { width: 24px; height: 24px; }
  .contact-web { color: var(--text-soft); }
  .bottom-strip {
    position: absolute; left: 0; bottom: 0; width: 100%; height: 14px;
    background: var(--brand-blue);
  }
</style>
</head>
<body>
  <div class="card">
    <header class="brand-band">
      <div class="brand-mark"></div>
      <h1 class="company-name">Q&amp;Q Fabrications, Inc.</h1>
    </header>

    <div class="person-row">
      <span class="person-name">Mark Halvorsen</span>
      <span class="person-title">CEO / Project Manager</span>
    </div>

    <div class="portrait" role="img" aria-label="Portrait photo of the project manager"></div>

    <section class="contact-panel">
      <ul class="contact-list">
        <li class="contact-item">
          <span class="contact-icon"><svg viewBox="0 0 24 24" fill="none" stroke="#fff" stroke-width="2"><rect x="3" y="6" width="18" height="12"/><path d="M3 6l9 7 9-7"/></svg></span>
          mark.halvorsen@qqfabrications-example.com
        </li>
        <li class="contact-item">
          <span class="contact-icon"><svg viewBox="0 0 24 24" fill="none" stroke="#fff" stroke-width="2"><rect x="4" y="7" width="16" height="11" rx="1"/></svg></span>
          555-010-2040
        </li>
        <li class="contact-item">
          <span class="contact-icon"><svg viewBox="0 0 24 24" fill="#fff"><path d="M6.6 10.8a15 15 0 006.6 6.6l2.2-2.2c.3-.3.7-.4 1-.2 1.1.4 2.3.6 3.6.6.6 0 1 .4 1 1V20c0 .6-.4 1-1 1A17 17 0 013 4c0-.6.4-1 1-1h3.5c.6 0 1 .4 1 1 0 1.3.2 2.5.6 3.6.1.3 0 .7-.2 1z"/></svg></span>
          555-010-2041
        </li>
        <li class="contact-item">
          <span class="contact-icon"><svg viewBox="0 0 24 24" fill="#fff"><path d="M12 2a7 7 0 00-7 7c0 5 7 13 7 13s7-8 7-13a7 7 0 00-7-7zm0 9.5A2.5 2.5 0 1112 6.5a2.5 2.5 0 010 5z"/></svg></span>
          1450 Orchard Lane Fairview, WI 53000
        </li>
        <li class="contact-item contact-web">
          <span class="contact-icon"><svg viewBox="0 0 24 24" fill="none" stroke="#fff" stroke-width="1.8"><circle cx="12" cy="12" r="9"/><ellipse cx="12" cy="12" rx="4" ry="9"/><path d="M3 12h18M5 7h14M5 17h14"/></svg></span>
          www.qqfabrications-example.com
        </li>
      </ul>
    </section>

    <div class="bottom-strip"></div>
  </div>
</body>
</html>
```